Historic Church website

We want our church website to feel warm, historic, and clean, modern, and easy to navigate. Dont use the anchor

Current website: https://www.meadowlarkchapelhall.com/

Requirements
Should not have
• I would like to use the logo without the anchor

```html
<!DOCTYPE html>
<html lang="en">
<head>
<meta charset="utf-8">
<title>Meadowlark Chapel Hall</title>
<link rel="stylesheet" href="https://fonts.googleapis.com/css2?family=Playfair+Display:wght@600;700&family=Montserrat:wght@400;500;600;700&family=Oswald:wght@500;600&display=swap">
<style>
:root{
  --ink:#18140f;
  --dark:#211b16;
  --dark-2:#2b231d;
  --wood-light:#d8c5a6;
  --wood-mid:#bfa682;
  --cream:#f1e9dc;
  --tan:#c8ab80;
  --tan-deep:#a88858;
  --text-light:#eee4d3;
  --text-muted:#b9ab96;
  --brown-text:#3a2a1c;
  --white:#ffffff;
  --card:#f4efe7;
}
*{box-sizing:border-box;margin:0;padding:0}
html,body{width:1200px;height:5097px;overflow:hidden}
body{background:var(--dark);font-family:"Montserrat",sans-serif;color:var(--text-light);position:relative}
section,header,footer{position:absolute;left:0;width:1200px}
.abs{position:absolute}
.serif{font-family:"Playfair Display",serif}
.label{font-family:"Montserrat",sans-serif;font-weight:600;font-size:13px;letter-spacing:2px;text-transform:uppercase;color:var(--tan);display:flex;align-items:center;gap:8px}
.label .dot{width:10px;height:10px;border:2px solid var(--tan);border-radius:50%}
.h2{font-family:"Playfair Display",serif;font-weight:700;font-size:42px;line-height:1.15;color:var(--white)}
.btn{display:inline-flex;align-items:center;gap:10px;background:var(--tan);color:var(--ink);font-weight:600;font-size:13px;letter-spacing:.5px;text-transform:uppercase;padding:12px 20px;border-radius:3px}
.btn .circ{width:16px;height:16px;border:1.5px solid var(--ink);border-radius:50%;display:flex;align-items:center;justify-content:center;font-size:9px}
.ph{border-radius:0}

/* header + hero */
.hero{top:0;height:740px;background:linear-gradient(90deg,#15110d 0%,#1d1712 45%,#2a2119 100%)}
.hero-photo{left:480px;top:0;width:720px;height:700px;background:radial-gradient(circle at 60% 55%,#6b5a42 0%,#3c3024 40%,#1d1712 78%)}
.topbar{top:18px;left:470px;display:flex;gap:210px;font-size:13px;color:var(--text-light)}
.topbar span{display:flex;align-items:center;gap:8px}
.topbar b{font-weight:600}
.logo{left:40px;top:20px;display:flex;flex-direction:column;align-items:center;gap:6px}
.logo .mark{width:74px;height:74px;border:2px solid var(--text-light);border-radius:50%;display:flex;align-items:center;justify-content:center;font-family:"Playfair Display",serif;font-weight:700;font-size:24px;color:var(--text-light)}
.nav{left:315px;top:62px;display:flex;align-items:center;gap:34px;font-size:14px;color:var(--text-light)}
.nav .active{font-weight:700;color:var(--white)}
.nav .btn{padding:9px 18px;margin-left:30px}
.hero-copy{left:105px;top:170px;width:460px}
.hero-copy .label{font-size:15px;margin-bottom:14px}
.hero-copy h1{font-family:"Playfair Display",serif;font-weight:700;font-size:62px;line-height:1.02;color:var(--white)}
.hero-copy p{margin-top:16px;font-size:15px;font-weight:500;letter-spacing:.5px;color:var(--text-light)}
.hero-copy .btn{margin-top:30px}

/* scripture band */
.scripture{top:680px;height:250px}
.scripture .quote{left:0;top:110px;width:1200px;text-align:center;font-family:"Oswald",sans-serif;font-weight:600;font-size:36px;line-height:1.25;color:var(--brown-text);letter-spacing:.5px}

/* about */
.about{top:930px;height:580px;background:var(--dark)}
.about-frame{left:128px;top:60px;width:300px;height:440px}
.about-copy{left:612px;top:100px;width:490px}
.about-copy .h2{margin:10px 0 20px}
.about-copy p{font-size:13px;line-height:1.75;color:var(--text-muted)}
.about-copy .btn{margin-top:22px}

/* visit */
.visit{top:1510px;height:640px;background:linear-gradient(180deg,#1f1a15,#2a221b 60%,#221c17)}
.center-head{left:0;width:1200px;text-align:center}
.center-head .label{justify-content:center}
.center-head .h2{margin-top:8px;font-size:36px}
.cards3{left:108px;top:160px;display:flex;gap:53px}
.vcard{width:295px;height:390px;background:var(--white);border-radius:6px;overflow:hidden;position:relative;color:var(--ink);text-align:center}
.vcard .img{height:250px}
.vcard h3{font-family:"Playfair Display",serif;font-weight:700;font-size:18px;margin-top:40px}
.vcard .time{font-size:13px;margin-top:8px;display:flex;justify-content:center;align-items:center;gap:6px}
.vcard.flipped .overlay{position:absolute;left:0;top:0;width:100%;height:100%;background:linear-gradient(180deg,rgba(20,16,12,.35),rgba(20,16,12,.82));display:flex;flex-direction:column;justify-content:center;align-items:center;padding:30px;color:var(--white);font-size:14px;line-height:1.5}
.vcard.flipped .overlay h3{color:var(--white);margin:60px 0 6px;font-size:20px}

/* independent */
.indep{top:2150px;height:640px;background:var(--cream)}
.indep-photo{left:640px;top:40px;width:560px;height:560px}
.indep-copy{left:105px;top:110px;width:480px}
.indep-copy .label{color:var(--brown-text)}
.indep-copy .label .dot{border-color:var(--brown-text)}
.indep-copy .h2{color:var(--ink);font-size:38px;margin:10px 0 16px}
.indep-copy p{font-size:13px;line-height:1.7;color:#4a3d30}
.indep-copy .btn{margin-top:22px}

/* sermon band */
.sermon{top:2790px;height:190px}
.sermon .quote{top:58px;left:0;width:1200px;text-align:center;font-family:"Oswald",sans-serif;font-weight:600;font-size:36px;line-height:1.25;color:var(--brown-text)}
.sermon .quote u{text-decoration-thickness:3px;text-underline-offset:4px}

/* testimonials */
.testi{top:2980px;height:580px;background:var(--dark)}
.tcards{left:108px;top:160px;display:flex;gap:53px}
.tcard{width:295px;height:300px;background:var(--card);border-radius:4px;position:relative;color:var(--ink);text-align:center;padding:36px 26px 0}
.tcard .q{position:absolute;left:-14px;top:-14px;width:34px;height:34px;border-radius:50%;background:var(--tan);color:var(--ink);font-family:"Playfair Display",serif;font-size:26px;line-height:38px}
.tcard .avatar{width:58px;height:58px;border-radius:50%;margin:0 auto;background:radial-gradient(circle at 50% 40%,#9a7e62,#4a382a)}
.tcard .stars{color:#e0a92a;font-size:13px;letter-spacing:2px;margin-top:10px}
.tcard h4{font-weight:700;font-size:15px;margin-top:8px}
.tcard .role{font-size:12px;color:#6b5f52;margin-top:2px}
.tcard p{font-size:13px;line-height:1.55;color:#3b3128;margin-top:14px}
.arrow-side{top:290px;color:var(--text-light);font-size:22px}
.dots{left:540px;top:523px;display:flex;gap:12px}
.dots i{width:9px;height:9px;border-radius:50%;background:#6a5c4d;display:block}
.dots i.on{background:var(--text-light);box-shadow:0 0 0 3px rgba(238,228,211,.25)}

/* events */
.events{top:3530px;height:530px;background:linear-gradient(180deg,#1a1511,#241d17)}
.events-head{left:105px;top:190px;width:300px}
.events-head .h2{font-size:36px;margin-top:10px}
.ev-arrows{margin-top:20px;display:flex;gap:10px}
.ev-arrows span{width:34px;height:34px;border-radius:50%;background:#4a3f35;display:flex;align-items:center;justify-content:center;font-size:14px;color:var(--white)}
.ev-arrows span.on{background:var(--text-light);color:var(--ink)}
.ecards{left:438px;top:110px;display:flex;gap:30px}
.ecard{width:300px;height:320px;background:var(--white);border-radius:6px;overflow:hidden;position:relative;color:var(--ink)}
.ecard .img{height:220px}
.ecard .date{position:absolute;right:14px;top:0;width:56px;height:66px;background:var(--white);border-radius:0 0 6px 6px;text-align:center;padding-top:6px;font-size:11px;font-weight:600;line-height:1.1}
.ecard .date b{display:block;font-family:"Playfair Display",serif;font-size:22px}
.ecard h3{font-family:"Playfair Display",serif;font-weight:700;font-size:19px;padding:18px 16px 6px}
.ecard .more{font-size:12px;font-weight:600;padding:0 16px;display:flex;align-items:center;gap:6px}

/* newsletter */
.news{top:4060px;height:480px;background:var(--cream)}
.news-art{left:0;top:40px;width:430px;height:440px;background:linear-gradient(135deg,rgba(200,180,150,.35),rgba(241,233,220,0) 75%)}
.news .center-head .label{color:var(--brown-text)}
.news .center-head .label .dot{border-color:var(--brown-text)}
.news .center-head .h2{color:var(--ink)}
.field{left:375px;width:450px;height:48px;background:var(--white);border-radius:3px;display:flex;align-items:center;gap:10px;padding:0 16px;font-size:13px;color:#6a5f54}
.news .btn{left:482px;top:372px;background:var(--ink);color:var(--white);position:absolute}
.news .btn .circ{border-color:var(--white)}

/* footer */
.footer{top:4540px;height:557px;background:#15110d}
.flogo{left:105px;top:90px;text-align:center;width:160px}
.flogo .name{font-family:"Playfair Display",serif;font-weight:700;font-size:24px;line-height:1.1;color:var(--text-light)}
.flogo p{font-size:10px;letter-spacing:1px;text-transform:uppercase;color:var(--text-muted);margin-top:20px;line-height:1.6}
.socials{display:flex;gap:10px;justify-content:center;margin-top:18px}
.socials i{width:28px;height:28px;border-radius:50%;background:var(--tan-deep);display:block}
.fcol h5{font-family:"Playfair Display",serif;font-weight:700;font-size:18px;color:var(--white);text-transform:uppercase;padding-bottom:10px;border-bottom:2px solid var(--tan);display:inline-block}
.fcol ul{list-style:none;margin-top:18px;font-size:13px;color:var(--text-light);line-height:2.3}
.contact-row{display:flex;gap:12px;margin-top:20px;font-size:13px;line-height:1.6}
.contact-row .ic{width:32px;height:32px;border-radius:50%;border:1.5px solid var(--tan);flex:none;display:flex;align-items:center;justify-content:center}
.contact-row b{color:var(--white)}
.thumbs{display:grid;grid-template-columns:repeat(3,80px);gap:10px;margin-top:20px}
.thumbs div{height:80px;border-radius:3px}
.copyright{left:0;top:500px;width:1200px;text-align:center;font-size:12px;color:var(--text-muted)}
.fline{left:105px;top:470px;width:990px;height:1px;background:#3a3028}
</style>
</head>
<body>

<section class="hero" aria-label="Welcome">
  <div class="abs hero-photo" role="img" aria-label="Photograph of old books resting on a wooden shelf in warm lamplight"></div>
  <div class="abs topbar">
    <span><svg width="16" height="16" viewBox="0 0 24 24" fill="none" stroke="#eee4d3" stroke-width="2"><rect x="3" y="5" width="18" height="14" rx="2"/><path d="M3 7l9 6 9-6"/></svg><b>Email :</b> info@meadowlarkchapelhall.com</span>
    <span><svg width="16" height="16" viewBox="0 0 24 24" fill="#eee4d3"><path d="M6.6 10.8a15 15 0 006.6 6.6l2.2-2.2a1 1 0 011-.25 11.4 11.4 0 003.6.57 1 1 0 011 1V20a1 1 0 01-1 1A17 17 0 013 4a1 1 0 011-1h3.5a1 1 0 011 1c0 1.25.2 2.45.57 3.6a1 1 0 01-.25 1z"/></svg><b>Phone :</b> 555.010.4821</span>
  </div>
  <div class="abs logo"><div class="mark">MCH</div></div>
  <nav class="abs nav">
    <span class="active">Home</span><span>About MCH</span><span>Ministries</span><span>Bible Studies</span><span>Sermon Library</span>
    <span class="btn">Donate <span class="circ">›</span></span>
  </nav>
  <div class="abs hero-copy">
    <div class="label">Founded in 1928</div>
    <h1>Welcome to Meadowlark Chapel</h1>
    <p>ANCIENT CHURCH. ANCIENT FAITH. ETERNAL TRUTH.</p>
    <span class="btn">Join our community <span class="circ">›</span></span>
  </div>
</section>

<section class="scripture" aria-label="Scripture">
  <svg class="abs" style="left:0;top:0" width="1200" height="250" viewBox="0 0 1200 250" aria-hidden="true">
    <defs><linearGradient id="woodA" x1="0" y1="0" x2="1" y2="0"><stop offset="0" stop-color="#c9b391"/><stop offset=".5" stop-color="#e2d2b7"/><stop offset="1" stop-color="#c7ae8a"/></linearGradient></defs>
    <path d="M0 40 Q600 110 1200 40 L1200 250 L0 250 Z" fill="url(#woodA)"/>
    <path d="M0 40 Q600 110 1200 40" stroke="#efe3cf" stroke-width="3" fill="none"/>
    <circle cx="600" cy="70" r="16" fill="#211b16" stroke="#e2d2b7" stroke-width="3"/>
  </svg>
  <div class="abs quote">WE HAVE THIS HOPE AS AN ANCHOR FOR THE SOUL,<br>FIRM AND SECURE. - HEB 6:19</div>
</section>

<section class="about" aria-label="About">
  <svg class="abs about-frame" viewBox="0 0 300 440" aria-hidden="true">
    <defs><linearGradient id="bldg" x1="0" y1="0" x2="0" y2="1"><stop offset="0" stop-color="#b8b0a4"/><stop offset="1" stop-color="#5a5047"/></linearGradient></defs>
    <path d="M20 180 A130 130 0 0 1 280 180 L280 430 L20 430 Z" fill="#3a3028"/>
    <circle cx="150" cy="150" r="140" fill="none" stroke="#6e5c4a" stroke-width="16"/>
  </svg>
  <div class="abs" role="img" aria-label="Photograph of the chapel building's arched entrance" style="left:156px;top:88px;width:244px;height:244px;border-radius:50%;background:radial-gradient(circle at 50% 35%,#d7d0c4,#8a8076 60%,#4a4038)"></div>
  <div class="abs about-copy">
    <div class="label"><span class="dot"></span>Who we are</div>
    <h2 class="h2">About Meadowlark Chapel</h2>
    <p>To all who worship with us we offer a cordial welcome in the name of the Lord Jesus Christ. We endeavor to combine the warmth of gracious Christian hospitality with the fervor of a personal, devotional application of the great doctrines and eternal truths of God's Word. This church is committed to a Christ honoring</p>
    <span class="btn">Read more <span class="circ">›</span></span>
  </div>
</section>

<section class="visit" aria-label="Visit us this Sunday">
  <div class="abs center-head" style="top:68px">
    <div class="label"><span class="dot"></span>Visit us this Sunday</div>
    <h2 class="h2">Flip The Boxes For More Information</h2>
  </div>
  <div class="abs cards3">
    <div class="vcard">
      <div class="img" role="img" aria-label="Photograph of a study room with a framed map on the wall" style="background:linear-gradient(160deg,#8a7964,#4b3e31)"></div>
      <h3>Morning Worship Service</h3>
      <div class="time">◷ 11:00 AM</div>
    </div>
    <div class="vcard flipped">
      <div class="img" role="img" aria-label="Photograph of the fellowship hall with bookshelves" style="height:100%;background:linear-gradient(160deg,#5a4a3a,#2a221a)"></div>
      <div class="overlay">
        <h3>All Church Lunch</h3>
        <div>◷ 12:15 PM</div>
        <div style="font-size:12px;margin:4px 0">~Family Room ~</div>
        <div>Please join us for lunch after the service. Everyone is welcome!</div>
      </div>
    </div>
    <div class="vcard">
      <div class="img" role="img" aria-label="Photograph of an antique wall clock" style="background:radial-gradient(circle at 50% 45%,#d9d2c6,#7d7264 55%,#3e342b)"></div>
      <h3>Afternoon Adult Bible Study</h3>
      <div class="time">◷ 12:45 PM</div>
    </div>
  </div>
</section>

<section class="indep" aria-label="Independent Christian church">
  <div class="abs indep-photo" role="img" aria-label="Photograph of a desk with a globe, old map and books" style="clip-path:polygon(18% 0,100% 0,100% 100%,0 100%);background:linear-gradient(135deg,#a8865c,#5a4430 55%,#2c2119)"></div>
  <div class="abs indep-copy">
    <div class="label"><span class="dot"></span>Meadowlark Chapel Hall is</div>
    <h2 class="h2">An Independent Christian Church In The Protestant Tradition</h2>
    <p>Its central tenets are found in its Articles of Faith and include belief in, the Deity and Lordship of Jesus Christ, the Trinity, Jesus' perfect life, atoning death on the cross, bodily resurrection, and ascension; Jesus' literal return; the inerrancy of the Bible in its original manuscripts.</p>
    <span class="btn">Read more <span class="circ">›</span></span>
  </div>
</section>

<section class="sermon" aria-label="Weekly sermon">
  <svg class="abs" style="left:0;top:0" width="1200" height="190" viewBox="0 0 1200 190" aria-hidden="true">
    <defs><linearGradient id="woodB" x1="0" y1="0" x2="1" y2="0"><stop offset="0" stop-color="#c9b391"/><stop offset=".5" stop-color="#e2d2b7"/><stop offset="1" stop-color="#c7ae8a"/></linearGradient></defs>
    <rect width="1200" height="190" fill="url(#woodB)"/>
  </svg>
  <div class="abs quote">IF YOU CANNOT JOIN US IN PERSON<br><u>CLICK HERE</u> FOR THIS WEEK'S SERMON</div>
</section>

<section class="testi" aria-label="Testimonials">
  <div class="abs center-head" style="top:60px">
    <div class="label"><span class="dot"></span>Testimonial</div>
    <h2 class="h2">What Our Client Say About Us</h2>
  </div>
  <div class="abs arrow-side" style="left:60px">‹</div>
  <div class="abs arrow-side" style="left:1128px">›</div>
  <div class="abs tcards">
    <div class="tcard"><div class="q">“</div><div class="avatar" role="img" aria-label="Portrait photograph"></div><div class="stars">★★★★★</div><h4>Elias R. Thornton</h4><div class="role">MCH Founder</div><p>"The great need across evangelicalism is exposition of the Scriptures...(read more)"</p></div>
    <div class="tcard"><div class="q">“</div><div class="avatar" role="img" aria-label="Portrait photograph"></div><div class="stars">★★★★★</div><h4>J Harlan Whitcomb</h4><div class="role">Client</div><p>"Christians are called to God's service not only in church...(read more)"</p></div>
    <div class="tcard"><div class="q">“</div><div class="avatar" role="img" aria-label="Portrait photograph"></div><div class="stars">★★★★★</div><h4>J Morris Caldwell</h4><div class="role">Client</div><p>"To all who worship with us we extend a cordial welcome in the Name of Christ...(read more)"</p></div>
  </div>
  <div class="abs dots"><i class="on"></i><i></i><i></i></div>
</section>

<section class="events" aria-label="Upcoming events">
  <svg class="abs" style="left:0;top:0" width="1200" height="80" viewBox="0 0 1200 80" aria-hidden="true">
    <path d="M0 0 H1200 V30 Q900 80 600 40 T0 50 Z" fill="#211b16"/>
    <path d="M0 50 Q300 0 600 40 T1200 30" stroke="#eee4d3" stroke-width="3" fill="none"/>
  </svg>
  <div class="abs events-head">
    <div class="label"><span class="dot"></span>Latest event</div>
    <h2 class="h2">Upcoming MCH Events</h2>
    <div class="ev-arrows"><span>‹</span><span class="on">›</span></div>
  </div>
  <div class="abs ecards">
    <div class="ecard">
      <div class="img" role="img" aria-label="Photograph of a lamp-lit room for evening Bible study" style="background:linear-gradient(160deg,#b07a3e,#4a3424 60%,#241a12)"></div>
      <div class="date">WED<b>21</b>JAN</div>
      <h3>Wednesday Night Bible Study</h3>
      <div class="more">READ MORE ⊙</div>
    </div>
    <div class="ecard">
      <div class="img" role="img" aria-label="Photograph of old books stacked on a shelf" style="background:linear-gradient(160deg,#7a6a56,#3e3329 60%,#1f1913)"></div>
      <div class="date">WED<b>25</b>JAN</div>
      <h3>Sunday Service</h3>
      <div class="more">READ MORE ⊙</div>
    </div>
  </div>
</section>

<section class="news" aria-label="Newsletter">
  <div class="abs news-art" role="img" aria-label="Faint line illustration of the historic chapel"></div>
  <div class="abs center-head" style="top:90px">
    <div class="label"><span class="dot"></span>Newsletter</div>
    <h2 class="h2">Sign Up For Our Weekly Newsletter</h2>
  </div>
  <div class="abs field" style="top:218px">👤 Enter Your Name</div>
  <div class="abs field" style="top:282px">✉ Enter Your Email</div>
  <span class="btn">Subscribe now <span class="circ">›</span></span>
</section>

<footer class="footer" aria-label="Footer">
  <div class="abs flogo">
    <div class="name">Meadowlark<br>Chapel Hall</div>
    <p>Rooted in faith, serving<br>our neighbors since 1928</p>
    <div class="socials"><i></i><i></i><i></i><i></i></div>
  </div>
  <div class="abs fcol" style="left:335px;top:90px">
    <h5>Quick Link</h5>
    <ul><li>Home</li><li>About MCH</li><li>Ministries</li><li>Bible Studies</li><li>Sermon Library</li></ul>
  </div>
  <div class="abs fcol" style="left:500px;top:90px;width:270px">
    <h5>Quick Contact</h5>
    <div class="contact-row"><span class="ic"><svg width="14" height="14" viewBox="0 0 24 24" fill="#c8ab80"><path d="M12 2a7 7 0 00-7 7c0 5 7 13 7 13s7-8 7-13a7 7 0 00-7-7zm0 9.5A2.5 2.5 0 1112 6a2.5 2.5 0 010 5z"/></svg></span><div><b>Location :</b><br>2180 Meadowlark Avenue Fairhaven, California 90000</div></div>
    <div class="contact-row"><span class="ic"><svg width="14" height="14" viewBox="0 0 24 24" fill="#c8ab80"><path d="M6.6 10.8a15 15 0 006.6 6.6l2.2-2.2a1 1 0 011-.25 11.4 11.4 0 003.6.57 1 1 0 011 1V20a1 1 0 01-1 1A17 17 0 013 4a1 1 0 011-1h3.5a1 1 0 011 1c0 1.25.2 2.45.57 3.6a1 1 0 01-.25 1z"/></svg></span><div><b>Phone :</b><br>555.010.4821</div></div>
    <div class="contact-row"><span class="ic"><svg width="14" height="14" viewBox="0 0 24 24" fill="none" stroke="#c8ab80" stroke-width="2"><rect x="3" y="5" width="18" height="14" rx="2"/><path d="M3 7l9 6 9-6"/></svg></span><div><b>Email :</b><br>info@meadowlarkchapelhall.com</div></div>
  </div>
  <div class="abs fcol" style="left:815px;top:90px">
    <h5>MCH Sermons</h5>
    <div class="thumbs" role="img" aria-label="Sermon cover thumbnails">
      <div style="background:linear-gradient(135deg,#6e5a44,#2d241c)"></div>
      <div style="background:linear-gradient(135deg,#8a6e4c,#3a2d22)"></div>
      <div style="background:linear-gradient(135deg,#5e5448,#262019)"></div>
      <div style="background:linear-gradient(135deg,#7a6650,#2f261e)"></div>
      <div style="background:linear-gradient(135deg,#9a7b55,#3f3024)"></div>
      <div style="background:linear-gradient(135deg,#665446,#29211a)"></div>
    </div>
  </div>
  <div class="abs fline"></div>
  <div class="abs copyright">© Copyright 2026 | Meadowlark Chapel Hall. Fairhaven, California. All Rights Reserved</div>
</footer>

</body>
</html>
```